Wordpress site needed for company's Healthcare Web App

Healthcare web app needs wordpress web design for web site that provides an overview of the product, a page explaining key features, a blog, a press release announcement section, customer testimonials, contact us, sign up page, invite friends.

The website should use the color scheme including in the logo. This web site is not the app, this website will be used to introduce the app.

Target Market(s)

Doctors, enterprise healthcare professionals, patients who will use patient portals to access their health info. (not the app itself, but this site introduces the app)

Industry/Entity Type

Health Care

Coding

Coded - Design and coding required

Number of Pages Required

5+ page

Font styles to use
Sans Serif

Requirements
Must have
• This is a Wordpress based site.
• Product Overview, Key Product Features, Blog, Press Releases, Events, Embedded Videos explaining the product and demo'ing features, Sign Up Page for people interested,
Nice to have
• Uplifting Hero Image for Healthcare Tech, color scheme fitting with logo

```html
<!DOCTYPE html>
<html lang="en">
<head>
<meta charset="utf-8">
<title>VitalNote</title>
<link href="https://fonts.googleapis.com/css2?family=Roboto:wght@300;400;500;700&display=swap" rel="stylesheet">
<style>
:root{
  --teal:#1c7c96;
  --teal-dark:#15627a;
  --teal-light:#2a93ae;
  --ink:#333a40;
  --muted:#7d868c;
  --soft:#f1f3f4;
  --hero:#e4ecef;
  --line:#d6dde0;
  --white:#ffffff;
  --footer-bottom:#0f4d61;
}
*{box-sizing:border-box;margin:0;padding:0}
html,body{width:1200px;height:2828px;overflow:hidden}
body{font-family:'Roboto',Arial,sans-serif;color:var(--ink);background:var(--white);position:relative}
.site-header{height:44px;display:flex;align-items:center;justify-content:space-between;padding:0 40px 0 88px;background:var(--white);border-bottom:1px solid var(--line)}
.brand{display:flex;align-items:center;gap:8px;font-size:18px;font-weight:500;color:var(--teal)}
.brand-mark{width:14px;height:14px;background:var(--teal)}
.main-nav{display:flex;align-items:center;gap:28px;font-size:12px;color:var(--ink)}
.main-nav .active{color:var(--teal);border-bottom:2px solid var(--teal);padding-bottom:4px}
.btn-signup{border:1px solid var(--ink);padding:6px 12px;border-radius:3px}
.hero{height:476px;background:linear-gradient(90deg,var(--hero),#f3f6f7);position:relative}
.hero-photo{position:absolute;right:0;top:0;width:640px;height:476px;background:linear-gradient(180deg,#dbe6ea,#b9cdd4)}
.hero-copy{position:absolute;left:88px;top:222px;width:340px}
.hero-copy h1{font-weight:300;font-size:36px;color:var(--teal);margin-bottom:14px}
.hero-copy p{font-size:11px;color:var(--muted);line-height:1.5;margin-bottom:18px}
.btn{display:inline-block;background:var(--teal);color:var(--white);font-size:11px;padding:9px 14px;border-radius:2px}
.section-title{text-align:center;font-weight:300;font-size:28px;color:var(--ink)}
.features{height:500px;position:relative;background:var(--white)}
.features .section-title{padding-top:52px}
.features svg.arc{position:absolute;left:0;top:0}
.feature{position:absolute;width:200px;font-size:10px;color:var(--muted);line-height:1.5}
.feature h3{font-size:11px;font-weight:500;color:var(--ink);letter-spacing:.5px;margin-bottom:4px}
.feature.top{left:420px;top:150px;width:360px;text-align:center}
.feature.top h3{font-size:15px;color:var(--teal);font-weight:400}
.feature.l1{left:100px;top:280px}
.feature.l2{left:100px;top:420px}
.feature.r1{left:860px;top:280px}
.feature.r2{left:860px;top:420px}
.more-features{position:absolute;left:490px;top:392px;width:220px;height:108px;border-radius:110px 110px 0 0;background:var(--teal);color:var(--white);font-size:10px;text-align:center;padding-top:56px;letter-spacing:.5px}
.invite{height:80px;background:var(--teal);display:flex;align-items:center;justify-content:space-between;padding:0 88px}
.invite h2{font-weight:300;font-size:26px;color:var(--white)}
.btn-outline{border:1px solid var(--white);color:var(--white);font-size:10px;padding:8px 12px;border-radius:2px}
.blogs{height:460px;background:var(--soft);padding-top:52px}
.cards{display:flex;justify-content:center;gap:28px;margin-top:30px}
.card{width:454px;background:var(--white);box-shadow:0 1px 3px rgba(0,0,0,.08)}
.card-photo{height:150px}
.card-body{padding:18px 20px 16px}
.card-body h3{font-size:16px;font-weight:400;margin-bottom:8px}
.meta{font-size:9px;color:var(--muted);margin-bottom:10px;display:flex;gap:16px}
.card-body p{font-size:10px;color:var(--muted);line-height:1.5;margin-bottom:12px}
.read{font-size:10px;font-weight:500}
.video{height:340px;background:linear-gradient(135deg,#2f8fa8,#1c6f88);display:flex;align-items:center;justify-content:center;gap:16px}
.video h2{font-weight:300;font-size:28px;color:var(--white)}
.testimonials{height:320px;padding-top:56px}
.quotes{display:flex;justify-content:center;gap:28px;margin-top:28px}
.quote{width:300px}
.quote-box{border:1px solid var(--line);padding:12px 16px;font-size:10px;font-style:italic;color:var(--muted);line-height:1.5;height:86px;position:relative}
.quote-box::after{content:"";position:absolute;left:-1px;bottom:-14px;border-left:14px solid var(--teal);border-bottom:14px solid transparent}
.quote-name{font-size:11px;margin-top:22px}
.quote-role{font-size:9px;color:var(--muted);margin-top:2px}
.press{height:400px;background:var(--soft);padding-top:30px}
.press .cards{margin-top:24px}
.press .card-photo{height:140px}
.contact-bar{height:170px;background:var(--teal);display:flex;align-items:center;justify-content:space-between;padding:0 88px;color:var(--white)}
.contact-item{display:flex;align-items:center;gap:16px}
.contact-item strong{display:block;font-weight:400;font-size:18px}
.contact-item small{font-size:10px;opacity:.85}
.bottom-bar{height:38px;background:var(--footer-bottom);color:var(--white);font-size:10px;display:flex;align-items:center;justify-content:space-between;padding:0 40px}
</style>
</head>
<body>
<header class="site-header">
  <div class="brand"><span class="brand-mark"></span>VitalNote</div>
  <nav class="main-nav">
    <span class="active">Overview</span><span>Key Features</span><span>Blog</span><span>Press Release/Events</span><span>Testimonials</span><span>Contact Us</span><span class="btn-signup">Signup</span>
  </nav>
</header>

<section class="hero">
  <div class="hero-photo" role="img" aria-label="Doctor in white coat reviewing an x-ray with an older patient"></div>
  <div class="hero-copy">
    <h1>VitalNote</h1>
    <p>Keep your health records in one safe place and share them with your doctors whenever you need.</p>
    <span class="btn">Get Started</span>
  </div>
</section>

<section class="features">
  <h2 class="section-title">Features</h2>
  <svg class="arc" width="1200" height="500" viewBox="0 0 1200 500">
    <path d="M360 360 Q600 150 840 360" fill="none" stroke="#c7d0d4" stroke-dasharray="3 4"/>
    <circle cx="600" cy="255" r="12" fill="#fff" stroke="#1c7c96"/>
    <circle cx="480" cy="281" r="9" fill="#fff" stroke="#333a40"/>
    <circle cx="720" cy="281" r="9" fill="#fff" stroke="#333a40"/>
    <circle cx="408" cy="322" r="8" fill="#fff" stroke="#333a40"/>
    <circle cx="792" cy="322" r="8" fill="#fff" stroke="#333a40"/>
  </svg>
  <div class="feature top"><h3>FEATURE NUMBER 3</h3>This is a simple approach to tracking your health and wellness at once.</div>
  <div class="feature l1"><h3>FEATURE NUMBER 2</h3>Track lab results and share them with your care team easily.</div>
  <div class="feature l2"><h3>FEATURE NUMBER 1</h3>Book visits and get reminders for upcoming appointments.</div>
  <div class="feature r1"><h3>FEATURE NUMBER 4</h3>Manage your medications and refill requests in a few taps.</div>
  <div class="feature r2"><h3>FEATURE NUMBER 5</h3>Send secure messages to your doctor from any device.</div>
  <div class="more-features">MORE FEATURES</div>
</section>

<section class="invite">
  <h2>Invite your friends</h2>
  <span class="btn-outline">Invite Friends to use this App</span>
</section>

<section class="blogs">
  <h2 class="section-title">Blogs</h2>
  <div class="cards">
    <article class="card">
      <div class="card-photo" role="img" aria-label="Smiling doctors standing together in a clinic" style="background:linear-gradient(135deg,#e8eef0,#c9d6db)"></div>
      <div class="card-body">
        <h3>Blog Heading here</h3>
        <div class="meta"><span>By: admin</span><span>Posted on: 26 July 2016</span></div>
        <p>Simple tips for keeping your records up to date, and why sharing them with your doctor helps every visit go faster and smoother.</p>
        <span class="read">Read More</span>
      </div>
    </article>
    <article class="card">
      <div class="card-photo" role="img" aria-label="Doctor with stethoscope talking to a patient" style="background:linear-gradient(135deg,#efe9e4,#cfc4bb)"></div>
      <div class="card-body">
        <h3>Blog Heading here</h3>
        <div class="meta"><span>By: admin</span><span>Posted on: 26 July 2016</span></div>
        <p>How patient portals help families follow care plans, view test results and stay in touch with their care team from home.</p>
        <span class="read">Read More</span>
      </div>
    </article>
  </div>
</section>

<section class="video">
  <h2>Watch Video Tutorial</h2>
  <svg width="34" height="34" viewBox="0 0 34 34"><circle cx="17" cy="17" r="16" fill="#fff"/><path d="M14 11 L23 17 L14 23Z" fill="#1c7c96"/></svg>
</section>

<section class="testimonials">
  <h2 class="section-title">Customer Testimonial</h2>
  <div class="quotes">
    <div class="quote"><div class="quote-box">"Now all my records are in one place. I can share results with my doctor before I even arrive at the clinic."</div><div class="quote-name">Robert Doe</div><div class="quote-role">Patient, City</div></div>
    <div class="quote"><div class="quote-box">"Our staff spends less time on calls. Patients see their lab results and book visits on their own."</div><div class="quote-name">Jane Clark</div><div class="quote-role">Clinic Manager</div></div>
    <div class="quote"><div class="quote-box">"Clear and simple to use. My parents manage their medicine lists without needing my help anymore."</div><div class="quote-name">Frank Brown</div><div class="quote-role">Caregiver, Town</div></div>
  </div>
</section>

<section class="press">
  <h2 class="section-title">Press Release &amp; Events</h2>
  <div class="cards">
    <article class="card">
      <div class="card-photo" role="img" aria-label="Woman with a cold holding a tissue" style="background:linear-gradient(135deg,#c9423e,#e9b39c)"></div>
      <div class="card-body">
        <h3>Press release heading here</h3>
        <div class="meta"><span>By: admin</span><span>Posted on: 26 July 2016</span></div>
        <p>We announce a new release that brings faster sync and shared family accounts to every user of the platform.</p>
        <span class="read">Read More</span>
      </div>
    </article>
    <article class="card">
      <div class="card-photo" role="img" aria-label="Doctor examining a young child in bed" style="background:linear-gradient(135deg,#dfe8ec,#b8ccd4)"></div>
      <div class="card-body">
        <h3>Any Event heading here</h3>
        <div class="meta"><span>By: admin</span><span>Posted on: 26 July 2016</span></div>
        <p>Join our team at the health tech meetup this fall to see a live demo and talk with our product team.</p>
        <span class="read">Read More</span>
      </div>
    </article>
  </div>
</section>

<footer>
  <div class="contact-bar">
    <div class="contact-item">
      <svg width="30" height="30" viewBox="0 0 24 24" fill="none" stroke="#fff" stroke-width="1.5"><path d="M5 3h4l2 5-3 2a12 12 0 0 0 6 6l2-3 5 2v4a2 2 0 0 1-2 2A17 17 0 0 1 3 5a2 2 0 0 1 2-2z"/></svg>
      <div><strong>( 123 ) 456 - 7890</strong><small>Mon to Fri 9am - 5:00 pm</small></div>
    </div>
    <div class="contact-item">
      <svg width="30" height="30" viewBox="0 0 24 24" fill="none" stroke="#fff" stroke-width="1.5"><rect x="3" y="5" width="18" height="14"/><path d="M3 5l9 8 9-8"/></svg>
      <div><strong>info@vitalnote.com</strong><small>Email us</small></div>
    </div>
    <div class="contact-item">
      <svg width="30" height="30" viewBox="0 0 24 24" fill="none" stroke="#fff" stroke-width="1.5"><path d="M12 22s7-7 7-12a7 7 0 0 0-14 0c0 5 7 12 7 12z"/><circle cx="12" cy="10" r="2.5"/></svg>
      <div><strong>Some address live goes here...</strong><small>Web Address: www.vitalnote.com</small></div>
    </div>
  </div>
  <div class="bottom-bar"><span>© VitalNote</span><span>Terms &amp; Conditions &nbsp;|&nbsp; Privacy Policy</span></div>
</footer>
</body>
</html>
```